Harbor Reel Works Needs A Web Layout Design
Aqua/Black/White used on the layout
Creative Brief
Entertainment
Harbor reel works is a company that deals with videography, photography, and dj services. It uses the colours of blue, black, and white. The logo that can be used can be either of the following : http://www.velmorafind.example/images/vendor/300/230/harbor-logo.jpg or http://img18.pixelnookhost.example/img18/2856/26226344958409311344955.jpg . You can put demo tabs for the menu for now because those are not committed upon, and the body should look professional for the niche that his business is.
I like the clean and professional look but i hate having a lack of creativity within the design . Also i want it to show that we are the best and that the person coming to our website HAS TO GO WITH US, based on a POP of our website to their eye.
High Tech
aqua blue

```html
<!DOCTYPE html>
<html lang="en">
<head>
<meta charset="utf-8">
<title>Harbor Reel Works</title>
<link rel="stylesheet" href="https://fonts.googleapis.com/css2?family=Libre+Baskerville:wght@400&family=Open+Sans:wght@400&display=swap">
<style>
  :root {
    --ink: #03070c;
    --navy-deep: #071521;
    --navy: #0d2a3d;
    --aqua: #1f5a78;
    --aqua-glow: #3f8fb4;
    --silver: #b9c2c8;
    --white: #f3f5f6;
    --text-soft: #c9d2d8;
    --panel-glass: rgba(8, 16, 24, 0.82);
    --frame: rgba(160, 180, 195, 0.45);
  }
  * { margin: 0; padding: 0; box-sizing: border-box; }
  html, body { width: 1200px; height: 542px; overflow: hidden; background: var(--ink); }
  .page {
    position: relative; width: 1200px; height: 542px; overflow: hidden;
    background: linear-gradient(180deg, var(--ink) 0, var(--navy-deep) 96px, var(--navy) 110px, var(--navy) 440px, var(--navy-deep) 470px, var(--ink) 499px);
  }
  .header-band {
    position: absolute; left: 0; top: 0; width: 1200px; height: 96px;
    background: linear-gradient(180deg, #02050a 0, #0a1c2a 100%);
    border-bottom: 1px solid rgba(63, 143, 180, 0.35);
  }
  .backdrop-pattern {
    position: absolute; left: 0; top: 96px; width: 1200px; height: 380px;
    background: radial-gradient(ellipse at 50% 50%, rgba(63,143,180,0.35), rgba(13,42,61,0) 70%),
                linear-gradient(180deg, #12344a, #0b2233);
  }
  .ornament {
    position: absolute; top: 170px; width: 170px; height: 230px;
    background: radial-gradient(ellipse at 50% 50%, rgba(185,194,200,0.55), rgba(185,194,200,0.08) 70%);
    border-radius: 40%;
  }
  .ornament--left { left: 0; }
  .ornament--right { right: 0; }
  .brand {
    position: absolute; top: 14px; left: 0; width: 1200px; text-align: center;
  }
  .brand-mark {
    display: inline-block; width: 10px; height: 10px; border-radius: 50%;
    background: var(--aqua-glow); vertical-align: middle; margin-right: 10px;
  }
  .brand-name {
    font-family: "Libre Baskerville", serif; font-size: 15px; letter-spacing: 4px;
    color: var(--aqua-glow); text-transform: uppercase; vertical-align: middle;
  }
  .slide-back {
    position: absolute; left: 156px; top: 96px; width: 228px; height: 372px;
    border: 1px solid var(--frame);
    background: linear-gradient(180deg, #060b12 0, #0e2233 55%, #2a5a7c 72%, #0a1724 100%);
    box-shadow: 0 0 24px rgba(0,0,0,0.7);
  }
  .slide-front {
    position: absolute; left: 372px; top: 72px; width: 696px; height: 396px;
    border: 1px solid var(--frame);
    background: #0b1520;
    box-shadow: 0 0 30px rgba(0,0,0,0.8);
    overflow: hidden;
  }
  .slide-photo {
    position: absolute; left: 130px; top: 0; width: 566px; height: 396px;
    background: linear-gradient(90deg, #0f1c28 0, #2c3a48 30%, #8a8478 55%, #c9b7a6 68%, #5b5c60 85%, #1d2834 100%);
  }
  .slide-caption {
    position: absolute; left: 0; top: 0; width: 360px; height: 396px;
    background: linear-gradient(90deg, var(--panel-glass) 0, var(--panel-glass) 70%, rgba(8,16,24,0) 100%);
    padding: 102px 0 0 24px;
  }
  .slide-title {
    font-family: "Libre Baskerville", serif; font-weight: 400; font-size: 18px;
    color: var(--white); margin-bottom: 14px;
  }
  .slide-text {
    font-family: "Open Sans", sans-serif; font-size: 10.5px; line-height: 15px;
    color: var(--text-soft); width: 228px;
  }
  .slide-dots {
    position: absolute; left: 24px; top: 364px; display: flex; gap: 6px;
  }
  .slide-dots span { width: 5px; height: 5px; border-radius: 50%; background: rgba(243,245,246,0.45); }
  .slide-dots span.is-active { background: var(--white); }
  .slide-arrows { position: absolute; right: 16px; top: 352px; display: flex; gap: 4px; }
  .main-nav {
    position: absolute; left: 0; top: 499px; width: 1200px; height: 43px;
    background: linear-gradient(180deg, #0a0f14, #020407);
    border-top: 1px solid rgba(63,143,180,0.25);
    display: flex; justify-content: center; align-items: center;
  }
  .main-nav a {
    font-family: "Libre Baskerville", serif; font-size: 14px; color: var(--silver);
    text-decoration: none; padding: 0 22px; border-left: 1px solid rgba(185,194,200,0.18);
    line-height: 30px; position: relative;
  }
  .main-nav a:last-child { border-right: 1px solid rgba(185,194,200,0.18); }
  .main-nav a.is-current { color: var(--white); }
  .main-nav a.is-current::before {
    content: ""; position: absolute; left: 50%; top: -8px; margin-left: -5px;
    border-left: 5px solid transparent; border-right: 5px solid transparent;
    border-bottom: 5px solid var(--white);
  }
</style>
</head>
<body>
<div class="page">
  <div class="header-band"></div>
  <div class="backdrop-pattern" role="img" aria-label="Aqua ornamental background pattern"></div>
  <div class="ornament ornament--left" role="img" aria-label="Silver scroll ornament"></div>
  <div class="ornament ornament--right" role="img" aria-label="Silver scroll ornament"></div>

  <div class="brand">
    <span class="brand-mark"></span><span class="brand-name">Harbor Reel Works</span>
  </div>

  <div class="slide-back" role="img" aria-label="Night seascape photograph"></div>

  <div class="slide-front">
    <div class="slide-photo" role="img" aria-label="Portrait photograph of a stylised model with a paper parasol"></div>
    <div class="slide-caption">
      <h2 class="slide-title">1. Scelerisque sagittis lorem</h2>
      <p class="slide-text">Sed scelerisque sagittis lorem. Phasellus sodales. Nulla urna justo, vehicula iuscipit nec, molestie sed, tellus. Quisque justo. Nam libero leo, elementum in. Sed sceleris sagittis lorem. Phasellus sodales. Nulla urna justo, vehicula in, suscipit nec, molestie sed, tellus. Quisque justo. Nam libero leo, elementum in, elementum.</p>
    </div>
    <div class="slide-dots">
      <span class="is-active"></span><span></span><span></span><span></span><span></span><span></span><span></span>
    </div>
    <div class="slide-arrows">
      <svg width="18" height="18" viewBox="0 0 18 18" aria-label="Previous slide"><circle cx="9" cy="9" r="8.5" fill="#f3f5f6"/><path d="M10.5 5.5 7 9l3.5 3.5" stroke="#0b1520" stroke-width="1.6" fill="none"/></svg>
      <svg width="18" height="18" viewBox="0 0 18 18" aria-label="Next slide"><circle cx="9" cy="9" r="8.5" fill="#f3f5f6"/><path d="M7.5 5.5 11 9l-3.5 3.5" stroke="#0b1520" stroke-width="1.6" fill="none"/></svg>
    </div>
  </div>

  <nav class="main-nav">
    <a href="#" class="is-current">HOME</a>
    <a href="#">TYPOGRAPHY</a>
    <a href="#">PORTFOLIO</a>
    <a href="#">BLOG</a>
    <a href="#">POST</a>
    <a href="#">CONTACT</a>
  </nav>
</div>
</body>
</html>
```